2 Page Website in "wordpress"

We just bought rigadvisorsgroup.example and we need a 2 page website in wordpress coding. The top of the page should have a place to flash pictures of equipment examples that we consult on, selling or buying. "you can borrow pictures of all kinds of Dozers, Excavators, Backhoes, Mining Equipment from all over the Internet.

THE HOME PAGE
Then the first page needs to have 2 sections for general content, with links menu built in somewhere. We may add up to 10-15 links over time, so save some space for us. Then the 2nd page just needs to be a general contact form, for the buyer and seller. The 2 sections need to be set up for. 1.The buyer - Explanation - 2. For the Seller - Explanation -

THE FORM PAGE
There will be about 10 fields for general info so they can submit inquries, whether it is a seller contacting us to sell equipment, or a buyer wanting us to find them a specific piece of equipment. Just figure about 10 fields.

Logo
We need logo built in that represents equipment sales….

THIS MUST BE BUILT IN WORDPRESS CODE. It is our understanding that google is favoring websites built in wordpress.

Industry/Entity Type

Internet

Requirements
Must have
• Wordpress coded

```html
<!DOCTYPE html>
<html lang="en">
<head>
<meta charset="utf-8">
<title>Rig Advisors Group</title>
<link href="https://fonts.googleapis.com/css2?family=Arimo:wght@400;700&display=swap" rel="stylesheet">
<style>
:root{
  --amber:#fdb71d;
  --black:#000;
  --dark:#1e1e1e;
  --darker:#191919;
  --field:#4a4a4a;
  --white:#fff;
  --rule:#3a3a3a;
  --hero:#6f7377;
}
*{margin:0;padding:0;box-sizing:border-box}
html,body{width:1200px;height:1184px;overflow:hidden}
body{position:relative;background:var(--dark);font-family:"Arimo",Arial,sans-serif;color:var(--white)}
.abs{position:absolute}
.rock-backdrop{left:0;top:0;width:1200px;height:886px;
  background:radial-gradient(ellipse at 80% 20%,#6d6d6d 0%,#4b4b4b 30%,transparent 60%),
  linear-gradient(180deg,#3a3a3a 0%,#555 25%,#4a4a4a 50%,#333 70%,#2a2a2a 100%)}
.header-bar{left:0;top:0;width:1200px;height:101px;background:rgba(20,20,20,.72)}
.brand{left:100px;top:31px;display:flex;align-items:center;gap:12px}
.brand-square{width:40px;height:40px;background:var(--amber)}
.brand-name{font-size:22px;font-weight:700;color:var(--white);letter-spacing:.5px}
.search{left:873px;top:19px;width:227px;height:29px;background:#1c1c1c;border:1px solid #555}
.search span{position:absolute;left:10px;top:8px;font-size:12px}
.search-btn{position:absolute;right:0;top:0;width:32px;height:27px;background:var(--amber)}
.nav a{position:absolute;top:66px;font-size:14px;color:var(--white);text-decoration:none;white-space:nowrap}
.nav a.active{color:var(--amber)}
.nav-underline{left:555px;top:101px;width:70px;height:3px;background:var(--amber)}
.slider{left:100px;top:153px;width:700px;height:408px;
  background:linear-gradient(180deg,#7a7e82 0%,var(--hero) 100%)}
.caption{left:120px;top:392px;width:300px;height:84px;background:var(--black);padding:13px 0 0 7px}
.caption h2{font-size:25px;font-weight:700;color:var(--amber)}
.caption p{font-size:18px;margin-top:4px}
.dots{left:116px;top:499px;display:flex;gap:7px}
.dots i{width:12px;height:12px;border-radius:50%;background:var(--black)}
.dots i.on{background:var(--white)}
.quick{left:800px;top:153px;width:300px;height:408px;background:var(--black)}
.quick-head{height:51px;background:var(--amber);padding:15px 0 0 14px;font-size:18px;font-weight:700}
.role{display:flex;gap:14px;padding:18px 0 0 11px;font-size:14px;font-weight:700}
.role label{display:flex;align-items:center;gap:8px}
.role b{width:14px;height:14px;border-radius:50%;background:#555;display:inline-block;position:relative}
.role b.on::after{content:"";position:absolute;left:4px;top:4px;width:6px;height:6px;border-radius:50%;background:var(--white)}
.field{padding:0 12px}
.field span{display:block;font-size:12px;margin-bottom:3px}
.field div{height:24px;background:var(--field)}
.submit{margin:11px 0 0 11px;width:70px;height:28px;background:var(--amber);font-size:13px;font-weight:700;text-align:center;line-height:28px}
.welcome{left:100px;top:662px;width:700px}
.welcome h1{font-size:24px;color:var(--amber);font-weight:700}
.welcome p{margin-top:20px;font-size:14px;line-height:24px}
.side-links{left:821px;top:660px;width:279px;height:187px;background:var(--amber);padding:26px 16px 0}
.side-links a{display:block;color:#222;font-weight:700;font-size:14px;text-decoration:none;padding:6px 0 12px;border-bottom:1px dotted #f6e2a8;margin-bottom:9px}
.footer{left:0;top:886px;width:1200px;height:241px;background:var(--dark)}
.col{top:44px}
.col h3{font-size:14px;color:var(--amber);font-weight:700;margin-bottom:25px}
.col li{list-style:none;font-size:14px;line-height:24px}
.vline{top:50px;width:1px;height:182px;background:var(--rule)}
.social li{display:flex;align-items:center;justify-content:space-between;width:150px;height:48px;line-height:normal}
.social i{width:28px;height:28px;border-radius:50%;border:1px solid #555;display:block}
.bottom{left:0;top:1127px;width:1200px;height:57px;background:var(--darker);border-top:1px solid var(--rule);font-size:14px;line-height:52px}
.bottom span{display:block;width:1148px;text-align:center}
</style>
</head>
<body>
<div class="abs rock-backdrop" role="img" aria-label="Dark photograph of rocks and heavy machinery at a mining site"></div>
<header class="abs header-bar"></header>
<div class="abs brand"><span class="brand-square"></span><span class="brand-name">RIG ADVISORS GROUP</span></div>
<div class="abs search"><span>Search</span><div class="search-btn">
<svg width="32" height="27" viewBox="0 0 32 27"><circle cx="14" cy="12" r="6" fill="none" stroke="#fff" stroke-width="2"/><line x1="18.5" y1="16.5" x2="24" y2="22" stroke="#fff" stroke-width="2.5"/></svg></div></div>
<nav class="nav">
  <a class="active" style="left:565px">HOME</a>
  <a style="left:634px">ABOUT US</a>
  <a style="left:733px">SERVICES</a>
  <a style="left:831px">PRODUCTS</a>
  <a style="left:937px">FAQ’S</a>
  <a style="left:1005px">CONTACT US</a>
</nav>
<div class="abs nav-underline"></div>

<div class="abs slider" role="img" aria-label="Photograph of a yellow wheel loader with raised bucket on a work site"></div>
<div class="abs caption"><h2>Rig Advisors Group</h2><p>Heavy Machines Consultant</p></div>
<div class="abs dots"><i class="on"></i><i></i><i></i><i></i></div>

<aside class="abs quick">
  <div class="quick-head">Quick Contact</div>
  <div class="role"><label><b class="on"></b>Are you a Buyer</label><label><b></b>Are you a Seller</label></div>
  <div class="field" style="margin-top:27px"><span>Name</span><div></div></div>
  <div class="field" style="margin-top:9px"><span>Number</span><div></div></div>
  <div class="field" style="margin-top:9px"><span>Equipment Needed</span><div></div></div>
  <div class="field" style="margin-top:9px"><span>Quantity</span><div></div></div>
  <div class="field" style="margin-top:9px"><span>Location</span><div></div></div>
  <div class="submit">SUBMIT</div>
</aside>

<section class="abs welcome">
  <h1>Welcome to Rig Advisors Group</h1>
  <p>Lorem Ipsum is simply dummy text of the printing and typesetting industry. Lorem Ipsum has been the industry's standard dummy text ever since the 1500s, when an unknown printer took a galley of type and scrambled it to make a type specimen book. It has survived not only five centuries, but also the leap into electronic typesetting, remaining essentially unchanged. It was popularised in the 1960s with the release of Letterfast sheets containing Lorem Ipsum passages, and more recently with desktop publishing software like Alden PageSetter including versions of Lorem Ipsum.</p>
</section>
<div class="abs side-links"><a>Other Sites</a><a>Reviews</a><a>Reports</a></div>

<footer class="abs footer">
  <div class="abs col" style="left:100px"><h3>Menu Links</h3><ul><li>Home</li><li>About Us</li><li>Services</li><li>Products</li><li>FAQ’s</li><li>Contact Us</li></ul></div>
  <div class="abs vline" style="left:253px"></div>
  <div class="abs col" style="left:307px"><h3>Support</h3><ul><li>Terms &amp; Conditions</li><li>Privacy Policy</li><li>Legal Notice</li><li>Disclaimer</li></ul></div>
  <div class="abs vline" style="left:515px"></div>
  <div class="abs col" style="left:573px"><h3>Contact Us</h3><ul><li>Hallbrook Partners</li><li>Kastanienweg 48b</li><li>10999 Lindenfeld</li><li>Northland</li><li>Telephone: +00 12 34567890</li><li>E-mail: hello@rigadvisorsgroup.example</li></ul></div>
  <div class="abs vline" style="left:838px"></div>
  <div class="abs col social" style="left:894px"><h3>Connect With Us</h3><ul style="margin-top:-14px"><li>Circlebook<i></i></li><li>Chirper<i></i></li><li>Workednet<i></i></li></ul></div>
</footer>
<div class="abs bottom"><span>© 2014 Company Name ,All Rights Reserved</span></div>
</body>
</html>
```